I would like to design a flyer that I can put on car windows, inside peoples mailboxes. This flyer is to display Crestline Athletics and Wellness is now Open. I would like this to be a Free One Week Pass! I would like to have the following information on the flyer.
1) My logo - CRESTLINE ATHLETICS AND WELLNESS (I will upload the logo)
2) Hours of operation - Mon - Fri "5am - 10pm" Sat/Sun "6am -6pm"
3) Membership $59.00 "No Initiation Fee" Month to Month Membership.
Class are free. The Classes are Yoga, Salsa Classes, Bootcamps, HITT, Sports Performance,
4) Personal Training
5) Message Therapy
6) Address: 2871 Havelmoor Commerce Dr. Suite 213
Chantilly, VA 20347
7) mail@crestlineaw-example.com
8) Free One Week Pass

```html
<!DOCTYPE html>
<html lang="en">
<head>
<meta charset="utf-8">
<title>Crestline Athletics and Wellness – Flyer</title>
<link rel="stylesheet" href="https://fonts.googleapis.com/css2?family=Oswald:wght@500&family=Open+Sans:wght@400;700&display=swap">
<style>
  :root {
    --page-bg: #eceef0;
    --paper: #ffffff;
    --ink: #1a1a1a;
    --brand-red: #d8232a;
    --tile-dark: #1c1c1e;
    --tile-dark-soft: #3a3a3c;
    --tile-red: #c8161d;
    --tile-red-deep: #7d0b0f;
    --tile-green: #2f9a3a;
    --tile-green-deep: #1b6a25;
    --white: #ffffff;
  }
  * { box-sizing: border-box; margin: 0; padding: 0; }
  html, body { width: 1200px; height: 720px; overflow: hidden; }
  body { background: var(--page-bg); font-family: "Open Sans", Arial, sans-serif; }

  .flyer {
    position: absolute; left: 350px; top: 10px;
    width: 500px; height: 700px;
    background: var(--paper);
    display: flex; flex-direction: column;
  }
  .flyer-header {
    height: 200px; display: flex; flex-direction: column;
    align-items: center; justify-content: center; gap: 26px;
  }
  .brand { display: flex; align-items: center; gap: 12px; }
  .brand-dot { width: 46px; height: 46px; border-radius: 50%; background: var(--brand-red); }
  .brand-name {
    font-family: "Open Sans", Arial, sans-serif; font-weight: 400;
    font-size: 17px; letter-spacing: 2px; color: var(--brand-red);
  }
  .details { text-align: center; font-size: 10.5px; line-height: 14px; color: var(--ink); }

  .grid {
    flex: 1; display: grid;
    grid-template-columns: repeat(3, 1fr); grid-template-rows: repeat(3, 1fr);
  }
  .tile { position: relative; overflow: hidden; }
  .photo-dark { background: radial-gradient(circle at 50% 45%, var(--tile-dark-soft), var(--tile-dark) 70%); }
  .photo-red { background: radial-gradient(circle at 55% 40%, var(--tile-red), var(--tile-red-deep) 85%); }
  .photo-green { background: radial-gradient(circle at 50% 30%, #47b34f, var(--tile-green) 50%, var(--tile-green-deep)); }

  .tile-label {
    position: absolute; inset: 0; display: flex; align-items: center; justify-content: center;
    text-align: center; font-family: "Oswald", "Arial Narrow", sans-serif; font-weight: 500;
    color: var(--white); font-size: 20px; line-height: 28px; text-transform: uppercase;
  }
  .membership {
    grid-column: 1 / span 2; display: flex; align-items: center;
    padding: 0 20px; color: var(--white); font-size: 12.5px; line-height: 17px;
  }
  .membership strong { font-weight: 700; }
  .free-pass {
    position: absolute; inset: 0; padding: 8px 0 0 22px;
    font-family: "Oswald", "Arial Narrow", sans-serif; font-weight: 500;
    color: var(--white); text-transform: uppercase; line-height: 0.95;
  }
  .free-pass .small { font-size: 26px; }
  .free-pass .big { font-size: 64px; line-height: 60px; }
  .contact {
    position: absolute; left: 12px; right: 6px; bottom: 24px; color: var(--white);
    white-space: nowrap;
  }
  .contact .web { font-family: "Oswald", "Arial Narrow", sans-serif; font-weight: 500; font-size: 10px; line-height: 14px; }
  .contact .mail { font-size: 9px; line-height: 13px; }
</style>
</head>
<body>
  <article class="flyer">
    <header class="flyer-header">
      <div class="brand">
        <span class="brand-dot"></span>
        <span class="brand-name">CRESTLINE ATHLETICS AND WELLNESS</span>
      </div>
      <p class="details">
        Address: 2871 Havelmoor Commerce Dr. Suite 213<br>
        Chantilly, VA 20347<br>
        Hours of operation - Mon - Fri "5am - 10pm" Sat/Sun "6am 6-pm"
      </p>
    </header>

    <section class="grid">
      <div class="tile photo-dark" role="img" aria-label="Photo of a man doing a barbell curl on a dark background"></div>
      <div class="tile photo-red" role="img" aria-label="Red-toned photo of an athlete's back">
        <span class="tile-label">Message<br>Therapy</span>
      </div>
      <div class="tile photo-dark" role="img" aria-label="Photo of a woman gripping a barbell on the floor"></div>

      <div class="tile photo-dark membership" role="img" aria-label="Dark photo of athletes training with dumbbells">
        <p>Membership 59.00$ "No Initiation Fee" Month to Month Membership.<br>
        <strong>Class are free.</strong> The Classes are Yoga, Salsa Classes, Bootcamps, HITT, Sports Performance,</p>
      </div>
      <div class="tile photo-green" role="img" aria-label="Green-toned photo of an athlete">
        <div class="free-pass"><span class="small">One Week</span><br><span class="big">Free<br>Pass</span></div>
      </div>

      <div class="tile photo-red" role="img" aria-label="Red-toned photo of an arm lifting a dumbbell">
        <span class="tile-label">Personal<br>Training</span>
      </div>
      <div class="tile photo-dark" role="img" aria-label="Photo of a woman lifting dumbbells"></div>
      <div class="tile photo-dark" role="img" aria-label="Photo of a man holding a dumbbell out to the side">
        <div class="contact">
          <div class="web">WWW.CRESTLINEAW-EXAMPLE.COM</div>
          <div class="mail">mail@crestlineaw-example.com</div>
        </div>
      </div>
    </section>
  </article>
</body>
</html>
```